A online shop for solid wood need a Stationary design

A new online shop (in Austria and Germany) for solid wood and steel furniture (feldberg-formwerk) needs a Stationay design (letterhead, business card, envelope etc...). Dining tables, coffee tables, TV furniture and similar furniture will be sold. Everything will be custom made.

```html
<!DOCTYPE html>
<html lang="en">
<head>
<meta charset="utf-8">
<title>Feldberg Formwerk – Business Card</title>
<link rel="stylesheet" href="https://fonts.googleapis.com/css2?family=Roboto:wght@400;500;700&display=swap">
<style>
  :root {
    --brand-red: #ec1c24;
    --brand-red-soft: #f26a6f;
    --card-white: #ffffff;
    --ink-dark: #3a3a3a;
    --ink-grey: #6b6b6b;
    --backdrop: #e9e9e9;
  }
  * { margin: 0; padding: 0; box-sizing: border-box; }
  html, body {
    width: 1200px; height: 800px; overflow: hidden;
    background: var(--backdrop);
    font-family: "Roboto", Arial, sans-serif;
  }
  .stage {
    width: 1200px; height: 800px;
    display: flex; justify-content: center; align-items: center; gap: 80px;
  }
  .card {
    position: relative;
    width: 330px; height: 580px;
    box-shadow: 0 6px 18px rgba(0,0,0,0.12);
  }
  .card--front { background: var(--card-white); }
  .card--back { background: var(--brand-red); }

  .wordmark {
    display: flex; align-items: center; gap: 12px;
    font-weight: 700; text-transform: uppercase; letter-spacing: 2px;
  }
  .wordmark__square { width: 22px; height: 22px; flex: none; }
  .wordmark__name { font-size: 24px; line-height: 1.05; }

  .card--front .wordmark {
    position: absolute; top: 80px; left: 0; right: 0; justify-content: center;
    color: var(--brand-red);
  }
  .card--front .wordmark__square { background: var(--brand-red); }

  .contact {
    position: absolute; left: 56px; top: 300px; right: 30px;
    color: var(--ink-grey); font-size: 17px; line-height: 1.3;
  }
  .contact__name {
    color: var(--brand-red); font-weight: 700; font-size: 19px;
    text-transform: uppercase; letter-spacing: 0.5px;
  }
  .contact__role { color: var(--ink-dark); font-weight: 500; font-size: 16px; margin-bottom: 22px; }
  .contact__address { margin-bottom: 10px; }
  .contact__line { display: flex; align-items: center; gap: 10px; margin-top: 4px; }
  .contact__icon { width: 18px; height: 18px; flex: none; }

  .edge-band {
    position: absolute; top: 0; bottom: 0; width: 12px;
    background: var(--brand-red-soft);
  }
  .edge-band--left { left: 0; }
  .edge-band--right { right: 0; }

  .card--back .wordmark {
    position: absolute; top: 230px; left: 0; right: 0; justify-content: center;
    color: var(--card-white);
  }
  .card--back .wordmark__square { background: var(--card-white); }
  .back__web {
    position: absolute; bottom: 70px; left: 0; right: 0; text-align: center;
    color: var(--card-white); font-size: 15px;
  }
</style>
</head>
<body>
<main class="stage">
  <section class="card card--front">
    <div class="wordmark">
      <span class="wordmark__square"></span>
      <span class="wordmark__name">Feldberg<br>Formwerk</span>
    </div>
    <div class="contact">
      <p class="contact__name">Martin Kessler</p>
      <p class="contact__role">Managing Director</p>
      <p class="contact__address">Suite 12/48 Larch Lane<br>Fernhill, Victoria<br>Australia</p>
      <p class="contact__line">
        <svg class="contact__icon" viewBox="0 0 24 24"><path fill="#ec1c24" d="M6.6 10.8a15 15 0 0 0 6.6 6.6l2.2-2.2a1 1 0 0 1 1-.25 11.4 11.4 0 0 0 3.6.57 1 1 0 0 1 1 1V20a1 1 0 0 1-1 1A17 17 0 0 1 3 4a1 1 0 0 1 1-1h3.5a1 1 0 0 1 1 1c0 1.25.2 2.45.57 3.57a1 1 0 0 1-.25 1z"/></svg>
        +61 3 5550 0172
      </p>
      <p class="contact__line">
        <svg class="contact__icon" viewBox="0 0 24 24"><rect x="2" y="5" width="20" height="14" fill="#ec1c24"/><path d="M2 5l10 8 10-8" fill="none" stroke="#fff" stroke-width="1.6"/></svg>
        info@feldbergformwerk.com
      </p>
      <p class="contact__line">
        <svg class="contact__icon" viewBox="0 0 24 24" fill="none" stroke="#ec1c24" stroke-width="2"><circle cx="12" cy="12" r="9.5"/><ellipse cx="12" cy="12" rx="4" ry="9.5"/><path d="M2.5 12h19"/></svg>
        www.feldbergformwerk.com
      </p>
    </div>
  </section>

  <section class="card card--back">
    <div class="edge-band edge-band--left" role="img" aria-label="Decorative sawtooth border pattern"></div>
    <div class="edge-band edge-band--right" role="img" aria-label="Decorative sawtooth border pattern"></div>
    <div class="wordmark">
      <span class="wordmark__square"></span>
      <span class="wordmark__name">Feldberg<br>Formwerk</span>
    </div>
    <p class="back__web">www.feldbergformwerk.com</p>
  </section>
</main>
</body>
</html>
```